I am a highly experienced private practice psychotherapist serving high end clientele in the Wall Street area of New York City. I need electronic letterhead (that can also be printed) to use for bills, receipts, and correspondences.

My clients are very high end and are used to elegance and wealth. The letterhead should contain the following information: Marian T. Holcombe, LCSW 72 Pellham Street, Suite 2561 New York, NY 10087 Phone : (917) 555-3194 email: therapy@marianholcombelcsw.example website: www.marianholcombelcsw.example

Thank you for your designs. Please be advised that the letterhead will be used for bills/invoices; professional letters to other mental health professionals and doctors, as well as to attorneys. It needs to be highly professional in the same way that a law firm has professional and elegant letterhead, raher than whimsical or with spa designers. My letters end up as official documents.

```html
<!DOCTYPE html>
<html lang="en">
<head>
<meta charset="utf-8">
<title>Marian T. Holcombe, LCSW — Letterhead</title>
<link rel="stylesheet" href="https://fonts.googleapis.com/css2?family=Source+Sans+3:wght@600;700&display=swap">
<style>
  :root {
    --paper: #ffffff;
    --blue-deep: #0a22d6;
    --blue-bright: #4b8bff;
    --bar-blue: #0b2ee6;
    --footer-tint: #bccbff;
    --footer-ink: #2240e6;
    --light-ink: #ffffff;
  }
  html, body {
    margin: 0;
    padding: 0;
    width: 1200px;
    height: 847px;
    overflow: hidden;
    background: var(--paper);
  }
  .canvas {
    position: relative;
    width: 1200px;
    height: 847px;
    background: var(--paper);
    font-family: "Source Sans 3", "Myriad Pro", Arial, sans-serif;
  }
  .letterhead {
    position: absolute;
    left: 578px;
    top: 0;
    width: 622px;
    height: 847px;
    background: var(--paper);
    overflow: hidden;
  }
  .header-wave {
    position: absolute;
    left: 0;
    top: 0;
    width: 622px;
    height: 200px;
    display: block;
  }
  .side-bar {
    position: absolute;
    left: 0;
    top: 0;
    width: 33px;
    height: 847px;
    background: var(--bar-blue);
  }
  .practitioner-name {
    position: absolute;
    left: 19px;
    top: 12px;
    margin: 0;
    font-size: 28px;
    font-weight: 700;
    color: var(--light-ink);
    letter-spacing: 0.1px;
  }
  .office-address {
    position: absolute;
    right: 14px;
    top: 70px;
    margin: 0;
    font-style: normal;
    text-align: right;
    font-size: 15px;
    font-weight: 700;
    line-height: 21px;
    color: var(--light-ink);
  }
  .contact-footer {
    position: absolute;
    left: 33px;
    top: 744px;
    width: 589px;
    height: 103px;
    background: var(--footer-tint);
    text-align: center;
    color: var(--footer-ink);
    font-size: 17px;
    font-weight: 700;
    line-height: 24.5px;
    padding-top: 10px;
    box-sizing: border-box;
  }
  .contact-footer p { margin: 0; }
</style>
</head>
<body>
<div class="canvas">
  <section class="letterhead">
    <svg class="header-wave" viewBox="0 0 622 200" aria-hidden="true">
      <defs>
        <linearGradient id="waveFill" x1="0" y1="0" x2="1" y2="0">
          <stop offset="0" stop-color="var(--blue-bright)" style="stop-color:#4b8bff"/>
          <stop offset="0.55" stop-color="#1f4cf0"/>
          <stop offset="1" stop-color="#0a22d6"/>
        </linearGradient>
      </defs>
      <path d="M0 0 H622 V150 C560 178 430 192 335 172 C250 152 205 42 115 44 C62 46 22 88 0 130 Z" fill="url(#waveFill)"/>
    </svg>
    <div class="side-bar"></div>
    <h1 class="practitioner-name">Marian T. Holcombe, LCSW</h1>
    <address class="office-address">
      72 Pellham Street,<br>
      Suite 2561<br>
      New York,<br>
      NY 10087
    </address>
    <footer class="contact-footer">
      <p class="contact-phone">P : (917) 555-3194</p>
      <p class="contact-email">Email : therapy@marianholcombelcsw.example</p>
      <p class="contact-web">Web : www.marianholcombelcsw.example</p>
    </footer>
  </section>
</div>
</body>
</html>
```